Boutique Fitness Facility needs a new meal plan design that is as hot as our workouts!

We are about to host our 6 week Heatwave Reset program and we need to have a great looking meal plan handout created that we can give to all of our participants.

I have attached an example of our current full meal plan, for a reference only.

As in the example I've provided, I'd like to have certain areas color coded such as the proteins being Blue, Fats -yellow, Carbs - orange and veggies- green.

These colors will corollate to the Breakfast - snack - lunch - snack - Dinner graph that I've provided and would like to have added to the new handout.

I would like our logo placed at the top and beneath the logo have the text "Heatwave Reset Challenge"

The flyer should be of a summer influence in colors and design and
All text should be easy to read.

Thank you and I look forward to seeing your design!

```html
<!DOCTYPE html>
<html lang="en">
<head>
<meta charset="utf-8">
<title>PulseForge – Heatwave Reset Challenge Meal Plan</title>
<link rel="stylesheet" href="https://fonts.googleapis.com/css2?family=Roboto:wght@400;500;700&family=Montserrat:wght@700;800;900&family=Oswald:wght@400;500&family=Permanent+Marker&family=Caveat+Brush&display=swap">
<style>
:root{
  --stage:#6b6b6b;
  --paper:#ffffff;
  --ink:#1d1d1d;
  --black:#0c0c0c;
  --yellow:#f7d417;
  --protein:#1f5fb8;
  --fat:#e8c40c;
  --carb:#f07c1a;
  --veg:#38b52a;
  --hex-blue:#3c4fa8;
  --hex-orange:#f28c1e;
  --hex-green:#3aae23;
  --panel:#0b5cb4;
  --panel-deep:#084c99;
  --lime:#6cf03a;
  --sky:#5fd3ff;
  --text-light:#ffffff;
}
*{box-sizing:border-box;margin:0;padding:0}
html,body{width:1091px;height:1200px;overflow:hidden;background:var(--stage)}
.sheet{position:absolute;left:98px;top:20px;width:896px;height:1160px;background:var(--paper);overflow:hidden;font-family:"Roboto",sans-serif;color:var(--ink)}

.gym-photo{position:absolute;left:430px;top:0;width:466px;height:330px;
  background:linear-gradient(180deg,#2b2b2b 0%,#4a4a4a 55%,#8a8a8a 85%,rgba(255,255,255,0) 100%)}
.brush-band{position:absolute;left:0;top:0;width:520px;height:260px}
.brand{position:absolute;left:48px;top:38px;display:flex;align-items:center;gap:12px}
.brand-dot{width:22px;height:22px;border-radius:50%;background:var(--yellow)}
.brand-name{font-family:"Montserrat",sans-serif;font-weight:900;font-size:58px;color:var(--text-light);letter-spacing:-1px;line-height:1}
.challenge-title{position:absolute;left:46px;top:120px;font-family:"Permanent Marker",cursive;font-size:33px;color:var(--yellow);letter-spacing:-.5px;white-space:nowrap}

.sand{position:absolute;left:0;top:1000px;width:476px;height:160px;
  background:linear-gradient(180deg,rgba(255,255,255,0) 0%,#efe2cc 55%,#d8bf97 100%)}

.food-group{position:absolute;left:42px}
.group-head{display:flex;align-items:center;height:32px}
.group-icon{width:32px;height:32px;border-radius:50%;border:2px solid var(--c);background:#fff;position:relative;z-index:1;display:flex;align-items:center;justify-content:center}
.group-icon i{width:16px;height:16px;border-radius:50%;background:var(--c);opacity:.35;display:block}
.group-pill{margin-left:-6px;height:28px;padding:0 28px 0 16px;background:var(--c);color:#fff;font-family:"Montserrat",sans-serif;font-weight:800;font-size:19px;line-height:28px;border-radius:0 5px 5px 0}
.group-list{list-style:none;margin:6px 0 0 8px}
.group-list li{position:relative;padding-left:18px;font-size:13.6px;line-height:19px;color:var(--ink)}
.group-list li::before{content:"✓";position:absolute;left:0;top:3px;width:13px;height:13px;border-radius:50%;background:var(--c);color:#fff;font-size:9px;line-height:13px;text-align:center;font-weight:700}
.protein{--c:var(--protein);top:306px}
.fats{--c:var(--fat);top:574px}
.carbs{--c:var(--carb);top:702px}
.veg{--c:var(--veg);top:948px}

.meal{position:absolute;left:272px;width:172px;height:184px}
.meal svg{position:absolute;left:0;top:0}
.meal-icon{position:absolute;left:68px;top:52px;width:36px;height:36px;border-radius:50%;background:radial-gradient(circle,#f7b26a 0%,#9ecbe8 70%,rgba(255,255,255,0) 72%)}
.meal-name{position:absolute;left:0;width:172px;top:94px;text-align:center;font-family:"Roboto",sans-serif;font-weight:700;font-size:15px;letter-spacing:1px;color:#2a2a2a}
.breakfast{top:284px}
.lunch{top:598px}
.dinner{top:915px}

.snack{position:absolute;left:296px;width:124px;text-align:center}
.snack-bowl{width:68px;height:68px;margin:0 auto;border-radius:50%;background:radial-gradient(circle,#f2d7a3 0%,#e2553a 45%,#2f7ca4 75%)}
.snack-name{margin-top:12px;font-family:"Montserrat",sans-serif;font-weight:800;font-size:14px;color:var(--veg);line-height:16px}
.snack-note{font-family:"Roboto",sans-serif;font-weight:500;font-size:12px;color:#333;letter-spacing:.3px;line-height:16px}
.snack-one{top:480px}
.snack-two{top:794px}
.flow-arrow{position:absolute}

.tips-panel{position:absolute;left:476px;top:310px;width:420px;height:850px;background:linear-gradient(160deg,var(--panel) 0%,var(--panel) 55%,var(--panel-deep) 100%);border-top-left-radius:96px}
.starfish{position:absolute;left:740px;top:282px;width:96px;height:72px;border-radius:50%;background:radial-gradient(ellipse,#f26a2a 0%,#ee8a4f 55%,rgba(255,255,255,0) 72%)}
.tips-title{position:absolute;left:522px;top:355px;font-family:"Caveat Brush",cursive;font-size:37px;color:var(--yellow);white-space:nowrap;letter-spacing:-.5px}
.tips-intro{position:absolute;left:522px;top:410px;width:352px;font-size:15px;line-height:19.3px;color:var(--text-light)}

.timeline{position:absolute;left:551px;top:540px;width:0;height:568px;border-left:2px dashed #fff}
.timeline-end{position:absolute;left:546px;top:1103px;width:10px;height:10px;border-radius:50%;background:#fff}
.tip-num{position:absolute;left:515px;width:72px;height:72px;border-radius:50%;background:#fff;color:var(--panel);font-family:"Oswald",sans-serif;font-size:36px;line-height:72px;text-align:center;letter-spacing:-1px}
.tip{position:absolute;left:600px;width:282px;color:var(--text-light)}
.tip-head{font-family:"Montserrat",sans-serif;font-weight:700;font-size:21px;line-height:26px}
.tip-head em{font-style:normal;font-family:"Caveat Brush",cursive;font-weight:400;font-size:26px}
.tip-body{margin-top:5px;font-family:"Montserrat",sans-serif;font-weight:700;font-size:12.6px;line-height:17px}
.lime{color:var(--lime)}.gold{color:var(--yellow)}.orange{color:var(--carb)}.sky{color:var(--sky)}
</style>
</head>
<body>
<main class="sheet">
  <div class="gym-photo" role="img" aria-label="Photo of a woman and a man doing lunges in a gym"></div>
  <svg class="brush-band" viewBox="0 0 520 260" aria-hidden="true">
    <path fill="#0c0c0c" d="M0 0H470L500 40 482 96 460 150 438 190 418 208 380 214 330 232 290 238 250 250 214 246 190 236 120 236 60 238 0 244Z"/>
  </svg>

  <div class="brand"><span class="brand-name">PulseForge</span><span class="brand-dot"></span></div>
  <h1 class="challenge-title">HEATWAVE RESET CHALLENGE</h1>

  <div class="sand" role="img" aria-label="Photo of beach sand"></div>

  <section class="food-group protein">
    <div class="group-head"><span class="group-icon" role="img" aria-label="Protein food icon"><i></i></span><span class="group-pill">Protein</span></div>
    <ul class="group-list">
      <li>4-6 oz Chicken Breast</li><li>4-6oz Turkey Breast</li><li>4-6 oz Filet Mignon</li><li>4-6 oz Flank Steak</li><li>4-6 oz Salmon</li><li>4-6 oz Tuna</li><li>4-6 oz Cod</li><li>4-6 oz Cottage Cheese</li><li>4-6 oz Greek Yogurt</li><li>4-6 oz Tofu</li><li>3 -5 egg whites + 1 whole egg</li>
    </ul>
  </section>
  <section class="food-group fats">
    <div class="group-head"><span class="group-icon" role="img" aria-label="Fat food icon"><i></i></span><span class="group-pill">Fats</span></div>
    <ul class="group-list">
      <li>¼ - ½ Avocado</li><li>1 tbs Olive Oil</li><li>1 small handful Almonds,<br>Walnuts, Cashews</li>
    </ul>
  </section>
  <section class="food-group carbs">
    <div class="group-head"><span class="group-icon" role="img" aria-label="Grain icon"><i></i></span><span class="group-pill">Carbs</span></div>
    <ul class="group-list">
      <li>3 – 4oz Sweet Potato</li><li>¼ - ½ cup White Rice</li><li>¼ - ½ cup Quinoa</li><li>¼ - ½ cup Oatmeal</li><li>¾ cup Blueberries</li><li>¾ cup Strawberries</li><li>¾ cup Raspberries</li><li>1 med. Apple</li><li>1 small orange</li><li>1 small grapefruit</li>
    </ul>
  </section>
  <section class="food-group veg">
    <div class="group-head"><span class="group-icon" role="img" aria-label="Vegetable basket icon"><i></i></span><span class="group-pill">Vegetables</span></div>
    <ul class="group-list">
      <li>1 Scoop Powdered Greens</li><li>1 Cup Sautéed Spinach</li><li>1 Cup Sautéed Kale, Broccoli</li><li>1 Cup Sautéed Bell Pepper</li><li>1 Cup Sautéed Carrots</li><li>1 Cup Sautéed Zucchini</li>
    </ul>
  </section>

  <div class="meal breakfast">
    <svg width="172" height="184" viewBox="-6 -2 172 184" aria-hidden="true">
      <g fill="none" stroke-width="13" stroke-linecap="butt">
        <path d="M80 10 149 50 149 130" stroke="#3c4fa8"/>
        <path d="M149 130 80 170 11 130" stroke="#3aae23"/>
        <path d="M11 130 11 50 80 10" stroke="#f28c1e"/>
      </g>
      <g font-family="Roboto,sans-serif" font-weight="700" font-size="22" fill="#fff" text-anchor="middle">
        <circle cx="11" cy="50" r="20" fill="#f28c1e" stroke="#fff" stroke-width="3"/><text x="11" y="58">1</text>
        <circle cx="149" cy="50" r="20" fill="#3c4fa8" stroke="#fff" stroke-width="3"/><text x="149" y="58">1</text>
        <circle cx="80" cy="170" r="20" fill="#3aae23" stroke="#fff" stroke-width="3"/><text x="80" y="178">1</text>
      </g>
    </svg>
    <span class="meal-icon" role="img" aria-label="Breakfast food icon"></span>
    <span class="meal-name">BREAKFAST</span>
  </div>

  <div class="snack snack-one">
    <div class="snack-bowl" role="img" aria-label="Bowl of oats with strawberries"></div>
    <div class="snack-name">SNACK</div>
    <div class="snack-note">1/2 Portion of Protien</div>
  </div>
  <svg class="flow-arrow" style="left:430px;top:470px" width="30" height="90" viewBox="0 0 30 90" aria-hidden="true">
    <path d="M6 4C26 20 24 60 14 80M6 74 14 82 22 70" fill="none" stroke="#222" stroke-width="1.5"/>
  </svg>

  <div class="meal lunch">
    <svg width="172" height="184" viewBox="-6 -2 172 184" aria-hidden="true">
      <g fill="none" stroke-width="13">
        <path d="M80 10 149 50 149 130" stroke="#3c4fa8"/>
        <path d="M149 130 80 170 11 130" stroke="#3aae23"/>
        <path d="M11 130 11 50 80 10" stroke="#f28c1e"/>
      </g>
      <g font-family="Roboto,sans-serif" font-weight="700" font-size="22" fill="#fff" text-anchor="middle">
        <circle cx="11" cy="50" r="20" fill="#f28c1e" stroke="#fff" stroke-width="3"/><text x="11" y="58">1</text>
        <circle cx="149" cy="50" r="20" fill="#3c4fa8" stroke="#fff" stroke-width="3"/><text x="149" y="58">1</text>
        <circle cx="80" cy="170" r="20" fill="#3aae23" stroke="#fff" stroke-width="3"/><text x="80" y="178">1</text>
      </g>
    </svg>
    <span class="meal-icon" role="img" aria-label="Fish plate icon"></span>
    <span class="meal-name">LUNCH</span>
  </div>

  <div class="snack snack-two">
    <div class="snack-bowl" role="img" aria-label="Bowl of oats with strawberries"></div>
    <div class="snack-name">SNACK</div>
    <div class="snack-note">1/2 Portion of Protien</div>
  </div>
  <svg class="flow-arrow" style="left:262px;top:786px" width="30" height="90" viewBox="0 0 30 90" aria-hidden="true">
    <path d="M20 4C4 22 6 60 16 80M8 72 16 82 24 72" fill="none" stroke="#222" stroke-width="1.5"/>
  </svg>

  <div class="meal dinner">
    <svg width="172" height="184" viewBox="-6 -2 172 184" aria-hidden="true">
      <g fill="none" stroke-width="13">
        <path d="M80 10 149 50 149 130" stroke="#3c4fa8"/>
        <path d="M149 130 80 170 11 130" stroke="#3aae23"/>
        <path d="M11 130 11 50 80 10" stroke="#e8c40c"/>
      </g>
      <g font-family="Roboto,sans-serif" font-weight="700" font-size="22" fill="#fff" text-anchor="middle">
        <circle cx="11" cy="50" r="20" fill="#e8c40c" stroke="#fff" stroke-width="3"/><text x="11" y="58">1</text>
        <circle cx="149" cy="50" r="20" fill="#3c4fa8" stroke="#fff" stroke-width="3"/><text x="149" y="58">1</text>
        <circle cx="80" cy="170" r="20" fill="#3aae23" stroke="#fff" stroke-width="3"/><text x="80" y="178">1</text>
      </g>
    </svg>
    <span class="meal-icon" role="img" aria-label="Dinner bowl icon"></span>
    <span class="meal-name">DINNER</span>
  </div>

  <section class="tips-panel" aria-hidden="true"></section>
  <div class="starfish" role="img" aria-label="Starfish with sunglasses and a seashell"></div>
  <h2 class="tips-title">Fuel Your Heatwave Reset!</h2>
  <p class="tips-intro">This plan isn't about starving yourself - it's about sculpting a lean, toned physique by shredding fat while preserving muscle. Here's how to maximize your results:</p>

  <div class="timeline"></div>
  <div class="timeline-end"></div>

  <div class="tip-num" style="top:503px">01</div>
  <div class="tip" style="top:506px">
    <h3 class="tip-head">Eat Like a <em class="lime">Champion</em></h3>
    <p class="tip-body" style="margin-top:8px">Stick to this list as close as possible for maximum results, 7 Days A Week.</p>
  </div>

  <div class="tip-num" style="top:599px">02</div>
  <div class="tip" style="top:597px">
    <h3 class="tip-head">Burn More Than You<br><em class="gold">Consume</em></h3>
    <p class="tip-body">This is the golden rule! You need to burn more calories than you consume to create a deficit and force your body to tap into fat stores for energy.</p>
  </div>

  <div class="tip-num" style="top:748px">03</div>
  <div class="tip" style="top:747px">
    <h3 class="tip-head">Prioritize <em class="orange">Protein</em></h3>
    <p class="tip-body">Protein helps build and maintain muscle mass, which is crucial for boosting metabolism and burning more calories at rest.</p>
  </div>

  <div class="tip-num" style="top:864px">04</div>
  <div class="tip" style="top:862px">
    <h3 class="tip-head">Maximize <em class="gold">Sleep</em></h3>
    <p class="tip-body">When sleep-deprived, your body produces more ghrelin (hunger hormone) and less leptin (satiety hormone). Aim for 7-8 hours of quality sleep nightly.</p>
  </div>

  <div class="tip-num" style="top:980px">05</div>
  <div class="tip" style="top:977px">
    <h3 class="tip-head">Consistency is<br><em class="sky">King/Queen</em></h3>
    <p class="tip-body">Don't expect overnight results. Stick to your plan, track your progress, and celebrate small victories. Remember, slow and steady wins the shred race</p>
  </div>
</main>
</body>
</html>
```